Retractable Banners for Ridgeway Talent Alliance

We need to have 2 different retractable banners designed that will be used at a variety of events. We plan to have the banners printed through printovera.com. According to their site, specs are as follows:

Retractable banners are digitally printed on 12oz double-sided smooth vinyl. While the area on the retractable banners is 33 x 78, the customer will want to provide a file that has an area of 35 x 82 to account for bleed, with 3" of that vertical bleed at the bottom of the design. Recommended DPI is 150. Upload capacity for Retractable Banners is 100MP.

Banner #1:
Ridgeway Talent Alliance logo at top

Then the following text placed lower on the banner:

Creating Positive Impacts for Lane County Businesses (Heading)

Body of text: Ridgeway Talent Alliance is committed to enhancing the region's ability to meet the workforce needs of local employers through the investments of federal and state funds.

Banner #2:

Meeting the workforce needs of employers and individuals through partnerships and innovation.

You can check out some of our images (water drop, waves) and color schemes we use on our website at ridgewaytalent.org.

Target Market(s)

Job seekers, workforce development professionals, city leaders, company CEO's, community members, elected officials.

Industry/Entity Type

Events

Font styles to use
Serif
Sans Serif

Requirements
Must have
• -Be easy to read and understand
• - Must include Ridgeway Talent Alliance logo and text provided for each banner
Nice to have
• color ideas for banners: #0655a3; #0393ce; #00a990; #0355a3; #00a990; #33a6d7
Should not have
• Nothing that depicts gender

```html
<!DOCTYPE html>
<html lang="en">
<head>
<meta charset="UTF-8">
<title>Ridgeway Talent Alliance – Retractable Banners</title>
<link href="https://fonts.googleapis.com/css2?family=Nunito:wght@900&family=Heebo:wght@400;500&family=Bebas+Neue&family=Yellowtail&family=Open+Sans:wght@600&display=swap" rel="stylesheet">
<style>
  :root {
    --stage: #b8fdf0;
    --sky-light: #33a6d7;
    --sky-deep: #0655a3;
    --white: #ffffff;
    --orange: #f4783a;
    --orange-shadow: #7a2e10;
    --sea: #21b3c9;
    --sand: #d9c49d;
  }
  * { box-sizing: border-box; margin: 0; padding: 0; }
  html, body { width: 1200px; height: 1200px; overflow: hidden; }
  body { background: var(--stage); position: relative; }

  .banner {
    position: absolute;
    top: 108px;
    width: 406px;
    height: 950px;
    overflow: hidden;
    box-shadow: 0 2px 6px rgba(0, 40, 60, 0.35);
    color: var(--white);
  }
  .banner--business { left: 124px; background: var(--sky-light); }
  .banner--community {
    left: 656px;
    background: linear-gradient(180deg, var(--sky-deep) 0%, #0a5cb0 40%, #1b72c4 60%);
  }

  .brand {
    position: absolute;
    top: 84px;
    display: flex;
    align-items: center;
    gap: 9px;
    font-family: 'Heebo', sans-serif;
    font-weight: 500;
    font-size: 18px;
    letter-spacing: 1.5px;
    text-transform: uppercase;
    white-space: nowrap;
  }
  .banner--business .brand { left: 48px; }
  .banner--community .brand { left: 50%; transform: translateX(-50%); }
  .brand__dot { width: 16px; height: 16px; border-radius: 50%; background: var(--white); flex: none; }

  .business__headline {
    position: absolute;
    left: 48px;
    top: 204px;
    font-family: 'Nunito', sans-serif;
    font-weight: 900;
    font-size: 30px;
    line-height: 42px;
    text-transform: uppercase;
    letter-spacing: 0.2px;
  }
  .business__rule {
    position: absolute;
    left: 48px;
    top: 390px;
    width: 310px;
    height: 1px;
    background: rgba(255, 255, 255, 0.8);
  }
  .business__body {
    position: absolute;
    left: 48px;
    top: 416px;
    width: 320px;
    font-family: 'Heebo', sans-serif;
    font-weight: 400;
    font-size: 14.4px;
    line-height: 25px;
  }
  .business__photo {
    position: absolute;
    left: 0;
    bottom: 0;
    width: 100%;
    height: 338px;
    background: linear-gradient(180deg,
      var(--sky-light) 0%, #5cb8e0 30%, #2aa9b0 42%, #5fc3a8 52%,
      #c9d6cf 60%, #e3cfa6 72%, var(--sand) 100%);
  }

  .community__photo {
    position: absolute;
    left: 0;
    bottom: 0;
    width: 100%;
    height: 560px;
    background: linear-gradient(180deg,
      rgba(6, 85, 163, 0) 0%, #3b8fd6 18%, #8fc6ea 28%,
      var(--sea) 40%, #4cc7d3 52%, #a9d6d8 62%,
      #cdb991 74%, #b8a27c 100%);
  }
  .community__intro {
    position: absolute;
    left: 0;
    top: 196px;
    width: 100%;
    text-align: center;
    font-family: 'Yellowtail', cursive;
    font-size: 24px;
    line-height: 30px;
    transform: rotate(-7deg);
  }
  .community__audience {
    position: absolute;
    left: 0;
    width: 100%;
    text-align: center;
    font-family: 'Bebas Neue', sans-serif;
    color: var(--orange);
    text-shadow: 2px 2px 0 var(--orange-shadow);
    line-height: 1;
    text-transform: uppercase;
  }
  .community__audience--first { top: 282px; font-size: 55px; letter-spacing: 0.5px; }
  .community__audience--second { top: 332px; font-size: 70px; letter-spacing: 0.5px; }
  .community__rule {
    position: absolute;
    left: 74px;
    width: 258px;
    height: 1px;
    background: rgba(255, 255, 255, 0.85);
  }
  .community__rule--top { top: 417px; }
  .community__rule--bottom { top: 478px; }
  .community__method {
    position: absolute;
    left: 0;
    top: 423px;
    width: 100%;
    text-align: center;
    font-family: 'Open Sans', sans-serif;
    font-weight: 600;
    font-size: 18px;
    line-height: 26px;
    letter-spacing: 0.6px;
    text-transform: uppercase;
  }
</style>
</head>
<body>

  <section class="banner banner--business">
    <div class="business__photo" role="img" aria-label="Beach photograph with a sandcastle on the shore and turquoise sea under clear blue sky"></div>
    <div class="brand"><span class="brand__dot"></span>Ridgeway Talent Alliance</div>
    <h1 class="business__headline">Creating<br>positive impacts<br>for Lane County<br>businesses.</h1>
    <div class="business__rule"></div>
    <p class="business__body">Ridgeway Talent Alliance is committed to enhancing the region's ability to meet the workforce needs of local employers through the investments of federal and state funds.</p>
  </section>

  <section class="banner banner--community">
    <div class="community__photo" role="img" aria-label="Beach photograph with an open seashell holding a pearl on the sand, blurred sea behind"></div>
    <div class="brand"><span class="brand__dot"></span>Ridgeway Talent Alliance</div>
    <p class="community__intro">Meeting The<br>Workforce Needs Of</p>
    <h2 class="community__audience community__audience--first">Employers and</h2>
    <h2 class="community__audience community__audience--second">Individuals</h2>
    <div class="community__rule community__rule--top"></div>
    <p class="community__method">Through partnerships<br>and&nbsp; innovation.</p>
    <div class="community__rule community__rule--bottom"></div>
  </section>

</body>
</html>
```